LOOP 20th Anniversary Letterhead

LOOP – Guidance, Reach, and Insight – is Harbor Works’s premiere Frontline Associate training program. LOOP includes compliance training, professional development, skill building, and training for corporate and sector-specific initiatives for all Harbor Works Frontline Associates.

We are celebrating our 20th anniversary in 2017! We would like our letterhead and logo to include some nod to this 20th anniversary. We're open to ideas that showcases this great milestone for the program. We will use this letterhead to showcase our anniversary in multiple training and marketing mediums throughout the year.

Logo: We would like to include our current logo with something to call out our 20th anniversary; we won't need a totally new logo from scratch. This logo should go at the top of the letterhead. We will need to include the Harbor Works/Onward Bright logo in the footer of the letterhead. It can be smaller though.

Letterhead: This letterhead will be used both in portrait and landscape on 8 1/2 X 11 paper. Often we use this letterhead in PowerPoint for slides, as well as in a lesson plan. We need to include enough space write a title in the header.

We are open to a watermark, but would love to see letterheads with and without it.

I have included our current template and two logos (that should be used).
Updates

Project Deadline Extended
Reason: We would like to extend the deadline for this project to allow for more submissions and/or revision to current submissions. We are most interested in designs that include something about our 20th anniversary (1997 - 2017) in either our logo, the header/footer, or in a watermark.

Target Market(s)

Frontline Associates (hourly associates), Managers

Industry/Entity Type

Communication

Logo Text

LOOP 20th Anniversary

Font styles to use
Other font styles liked:
• Calibri; Century Gothic

Colors
6b449b
000000
cbcbcb

Requirements
Must have
• - Appropriate for web and print
• - EPS, JPEG, PNG
• - Purple (from the LOOP logo), black, and gray color scheme
• - Transparent
• - Space to put a title in the header
• - No more than 1 inch from the top
• - Portrait and Landscape to use on letterhead and PowerPoint
Nice to have
• - Maybe a watermark? <-- We are open to seeing designs with and without it.
• - Should look good when printed in color or black and white
Should not have
• - No stock images, clip art
• - Overly large graphics that take up too much space in the body of the letterhead. We will need to create text here.

```html
<!DOCTYPE html>
<html lang="en">
<head>
<meta charset="utf-8">
<title>LOOP 20th Anniversary Letterhead — Portrait Set</title>
<link rel="stylesheet" href="https://fonts.googleapis.com/css2?family=Questrial&display=swap">
<style>
  :root {
    --loop-purple: #4b2c92;
    --loop-violet: #6b449b;
    --ink: #000000;
    --ash: #cbcbcb;
    --paper: #ffffff;
    --backdrop: #c0c0c0;
    --watermark: #ebe9f3;
    --watermark-soft: #e4e2ec;
    --text-font: "Questrial", "Century Gothic", sans-serif;
  }
  * { box-sizing: border-box; margin: 0; padding: 0; }
  html, body {
    width: 1200px; height: 1200px; overflow: hidden;
    background: var(--backdrop);
    font-family: var(--text-font);
  }
  .set { position: relative; width: 1200px; height: 1200px; }
  .sheet {
    position: absolute; top: 324px;
    width: 403px; height: 522px;
    background: var(--paper);
    overflow: hidden;
  }
  .sheet--plain { left: 153px; }
  .sheet--watermark { left: 657px; }

  /* Header brand block with anniversary line */
  .brand {
    position: absolute; left: 38px; top: 34px;
    display: flex; flex-direction: column; gap: 4px;
  }
  .brand__row { display: flex; align-items: center; gap: 6px; }
  .brand__mark { width: 10px; height: 10px; background: var(--loop-purple); }
  .brand__name {
    font-size: 28px; letter-spacing: 1px; color: var(--loop-purple); line-height: 1;
  }
  .brand__anniversary {
    display: flex; align-items: center; gap: 5px;
    font-size: 7px; letter-spacing: 1.2px; color: var(--ink);
    text-transform: uppercase; white-space: nowrap;
  }
  .brand__years { color: var(--loop-violet); }
  .brand__dot { width: 3px; height: 3px; border-radius: 50%; background: var(--ash); }

  /* Faint centre watermark: name plus anniversary dates */
  .watermark {
    position: absolute; left: 96px; top: 240px; width: 200px;
    display: flex; flex-direction: column; align-items: center; gap: 8px;
  }
  .watermark__name {
    font-size: 62px; letter-spacing: 4px; color: var(--watermark); line-height: 1;
  }
  .watermark__years {
    font-size: 11px; letter-spacing: 3px; color: var(--watermark-soft);
    text-transform: uppercase; white-space: nowrap;
  }

  /* Footer */
  .footer {
    position: absolute; left: 38px; right: 0;
    display: flex; align-items: center;
    font-size: 5px; color: var(--ink); white-space: nowrap;
  }
  .sheet--plain .footer { top: 490px; }
  .sheet--watermark .footer { top: 497px; left: 48px; }
  .footer__partners { display: flex; align-items: center; gap: 5px; }
  .footer__partner { font-size: 7.5px; color: var(--ink); }
  .footer__divider { width: 1px; height: 8px; background: var(--ink); }
  .footer__divider--small { height: 5px; }
  .footer__contact { display: flex; align-items: center; gap: 4px; margin-left: 28px; }
  .sheet--plain .footer__contact { margin-left: 36px; }
  .footer__phone-icon { width: 6px; height: 5px; }

  .rule-thin {
    position: absolute; left: 152px; right: 0; top: 498px;
    height: 1px; background: var(--loop-violet);
  }
  .rule-double { position: absolute; left: 26px; width: 350px; top: 482px; }
  .rule-double__top { height: 1px; background: var(--loop-purple); }
  .rule-double__bottom { height: 4px; margin-top: 1px; background: var(--loop-purple); }
</style>
</head>
<body>
<main class="set">

  <section class="sheet sheet--plain" aria-label="Letterhead without watermark">
    <header class="brand">
      <div class="brand__row">
        <span class="brand__mark"></span>
        <span class="brand__name">LOOP</span>
      </div>
      <div class="brand__anniversary">
        <span class="brand__years">20 Years</span>
        <span class="brand__dot"></span>
        <span>1997 – 2017</span>
      </div>
    </header>
    <footer class="footer">
      <div class="footer__partners">
        <span class="footer__partner">Harbor Works</span>
        <span class="footer__divider"></span>
        <span class="footer__partner">Onward Bright</span>
      </div>
      <div class="footer__contact">
        <svg class="footer__phone-icon" viewBox="0 0 12 10" aria-hidden="true"><path d="M1 3 Q6 -1 11 3 L9 4 L8 3 Q6 2 4 3 L3 4 Z M3 5 H9 L10 9 H2 Z" fill="var(--loop-purple)"/></svg>
        <span>(555) 014-0120</span>
        <span class="footer__divider footer__divider--small"></span>
        <span>240 Lakeside Avenue, Suite 000, Milford, Ohio 00000</span>
      </div>
    </footer>
    <div class="rule-thin"></div>
  </section>

  <section class="sheet sheet--watermark" aria-label="Letterhead with watermark">
    <header class="brand">
      <div class="brand__row">
        <span class="brand__mark"></span>
        <span class="brand__name">LOOP</span>
      </div>
      <div class="brand__anniversary">
        <span class="brand__years">20 Years</span>
        <span class="brand__dot"></span>
        <span>1997 – 2017</span>
      </div>
    </header>
    <div class="watermark" aria-hidden="true">
      <span class="watermark__name">LOOP</span>
      <span class="watermark__years">1997 – 2017</span>
    </div>
    <div class="rule-double">
      <div class="rule-double__top"></div>
      <div class="rule-double__bottom"></div>
    </div>
    <footer class="footer">
      <div class="footer__partners">
        <span class="footer__partner">Harbor Works</span>
        <span class="footer__divider"></span>
        <span class="footer__partner">Onward Bright</span>
      </div>
      <div class="footer__contact">
        <svg class="footer__phone-icon" viewBox="0 0 12 10" aria-hidden="true"><path d="M1 3 Q6 -1 11 3 L9 4 L8 3 Q6 2 4 3 L3 4 Z M3 5 H9 L10 9 H2 Z" fill="var(--loop-purple)"/></svg>
        <span>(555) 014-0120</span>
        <span class="footer__divider footer__divider--small"></span>
        <span>240 Lakeside Avenue, Suite 000, Milford, Ohio 00000</span>
      </div>
    </footer>
  </section>

</main>
</body>
</html>
```